Online Fitness Coaching needs a Logo/Wordpress Web design

We need a Logo / Web design for our online company, that we are planning to start. Our many servcie is nutrition and training consulting for athletes who are looking for Physique changes (losing fat, building muscles), Powerlifters and Hybrid athletes (improving strength and endurance at the same time e.g Powerlifter who wants to compete in a PL Meet and a half marathon).
The Consulting is complete online so that the customer can train wherever she/he is and the price will be lower then a normal PT training and would be more time effective. We would like to have a Logo with represents the different sports Physique/PL/Hybrid training in one picture/logo e.g like a runner in the Logo.
Updates
Sick
Target Market(s)
Fitness sport market
Industry/Entity Type
Fitness
Coding
Coded - Design and coding required
Number of Pages Required
2 page
Colors
Designer to choose colors to be used in the design.
Look and feel
Each slider illustrates characteristics of the customer's brand and the style your logo design should communicate.

```html
<!DOCTYPE html>
<html lang="en">
<head>
<meta charset="utf-8">
<title>Peak Forge Athletics – Online Fitness Coaching</title>
<link rel="stylesheet" href="https://fonts.googleapis.com/css2?family=Oswald:wght@400;500;600&family=Open+Sans:wght@400;600&display=swap">
<style>
:root{
  --red:#b5121b;
  --red-dark:#8c0c13;
  --ink:#121212;
  --panel:#1b1b1b;
  --panel-2:#222;
  --line:#333;
  --text:#e9e9e9;
  --muted:#9a9a9a;
  --head:"Oswald",Impact,sans-serif;
  --body:"Open Sans",Arial,sans-serif;
}
*{box-sizing:border-box;margin:0;padding:0}
html,body{width:1200px;height:3296px;overflow:hidden}
body{background:var(--ink);color:var(--text);font-family:var(--body);font-size:15px;line-height:1.6}
.page{position:relative;width:1200px;height:3296px}

/* header + hero */
.hero{position:relative;height:660px;overflow:hidden}
.hero-photo{position:absolute;inset:0;background:radial-gradient(ellipse at 50% 45%,#6b5448 0%,#3a2f2a 28%,#1c1918 60%,#0d0d0d 100%)}
.site-header{position:absolute;top:0;left:0;right:0;height:130px;display:flex;justify-content:space-between;align-items:flex-start;padding:0 90px 0 120px}
.brand{margin-top:0;width:200px;height:130px;background:rgba(0,0,0,.75);display:flex;flex-direction:column;align-items:center;justify-content:flex-end;padding-bottom:20px;gap:8px}
.brand-mark{width:46px;height:46px;border-radius:50%;background:var(--text)}
.brand-name{font-family:var(--head);font-weight:500;font-size:17px;letter-spacing:1px;color:var(--text);text-transform:uppercase}
.main-nav{display:flex;gap:0;margin-top:34px}
.main-nav a{font-family:var(--head);font-size:15px;letter-spacing:1px;color:var(--text);text-decoration:none;padding:10px 20px}
.main-nav a.is-active{background:var(--red)}
.hero-copy{position:absolute;top:410px;left:0;right:0;text-align:center}
.hero-title{font-family:var(--head);font-weight:500;font-size:40px;letter-spacing:2px;text-transform:uppercase}
.hero-sub{font-family:var(--head);font-size:18px;letter-spacing:1px;margin-top:8px}
.hero-dots{position:absolute;top:622px;left:0;right:0;display:flex;justify-content:center;gap:12px}
.hero-dots span{width:14px;height:14px;border-radius:50%;border:2px solid #fff}
.hero-dots span.on{background:#fff}

/* welcome */
.welcome{height:300px;background:var(--red);text-align:center;padding-top:40px}
.section-title{font-family:var(--head);font-weight:500;font-size:32px;letter-spacing:1px;text-transform:uppercase}
.section-title em{font-style:normal;color:var(--red)}
.welcome p{width:900px;margin:22px auto 0;font-size:14px;line-height:1.75}
.btn{display:inline-block;font-family:var(--head);font-size:14px;letter-spacing:1px;text-transform:uppercase;color:#fff;padding:10px 24px;background:var(--red)}
.welcome .btn{background:var(--red-dark);margin-top:26px}

/* services */
.services{height:480px;text-align:center;padding-top:46px;border-bottom:1px solid #000}
.lead{font-size:14px;color:var(--muted);margin-top:16px}
.service-grid{display:flex;justify-content:center;gap:48px;margin-top:50px}
.service{width:240px}
.service-icon{width:100px;height:100px;margin:0 auto}
.service h3{font-family:var(--head);font-weight:500;font-size:17px;margin-top:20px;text-transform:uppercase}
.service p{font-size:13px;color:var(--muted);margin-top:8px;line-height:1.6}

/* about */
.about{height:480px;background:linear-gradient(#1a1a1a,#101010);display:flex;gap:50px;padding:60px 0 0 220px}
.about-photo{width:412px;height:348px;background:linear-gradient(135deg,#5a1d1d,#2c2424 45%,#4a3a33);border:1px solid #2a2a2a}
.about-copy{width:390px;padding-top:20px}
.about-copy p{font-size:13px;color:var(--muted);margin-top:18px;line-height:1.75}
.about-copy .btn{margin-top:28px}

/* pricing */
.pricing{height:620px;text-align:center;padding-top:30px}
.price-grid{display:flex;justify-content:center;gap:34px;margin-top:52px}
.plan{position:relative;width:316px;height:384px;background:var(--panel);border-top:2px solid #444;padding-top:46px}
.plan-dot{position:absolute;top:-18px;left:50%;width:36px;height:36px;margin-left:-18px;border-radius:50%;background:#444;border:8px solid var(--panel)}
.plan h3{font-family:var(--head);font-weight:400;font-size:15px;color:var(--muted);text-transform:uppercase;letter-spacing:1px}
.plan-price{margin:16px 0 10px;background:var(--panel-2);padding:10px 0;font-family:var(--head);font-size:22px}
.plan-price small{font-size:12px;color:var(--muted)}
.plan.featured .plan-price{background:var(--red)}
.plan.featured .plan-price small{color:#fff}
.plan ul{list-style:none}
.plan li{font-size:13px;color:var(--muted);padding:11px 0;border-bottom:1px solid var(--line);margin:0 30px}
.plan .btn{margin-top:26px;font-size:13px;padding:8px 20px}

/* blog */
.blog{height:500px;text-align:center;padding-top:40px;background:#151515}
.post-grid{display:flex;justify-content:center;gap:34px;margin-top:40px}
.post{width:320px;text-align:left}
.post-photo{height:200px}
.post h3{font-family:var(--head);font-weight:500;font-size:17px;margin-top:20px;text-transform:uppercase}
.post p{font-size:13px;color:var(--muted);margin-top:6px;line-height:1.55}
.post time{display:block;font-size:12px;color:var(--red);margin-top:8px}

/* footer */
.site-footer{height:256px;background:#0b0b0b;text-align:center;padding-top:50px}
.social{display:flex;justify-content:center;gap:20px}
.social span{width:44px;height:44px;border-radius:50%;border:2px solid #555}
.foot-nav{display:flex;justify-content:center;margin-top:48px}
.foot-nav a{font-family:var(--head);font-size:13px;letter-spacing:1px;color:var(--muted);text-decoration:none;padding:0 20px;border-right:1px solid #333}
.foot-nav a:last-child{border-right:0}
.copyright{font-size:12px;color:#666;margin-top:20px}
</style>
</head>
<body>
<div class="page">

<section class="hero">
  <div class="hero-photo" role="img" aria-label="Muscular athlete standing bare-chested in a dark gym with dumbbell racks"></div>
  <header class="site-header">
    <div class="brand"><span class="brand-mark"></span><span class="brand-name">Peak Forge Athletics</span></div>
    <nav class="main-nav">
      <a class="is-active" href="#">HOME</a><a href="#">ABOUT US</a><a href="#">SERVICES</a><a href="#">PRICING</a><a href="#">NEWS</a><a href="#">CONTACT US</a>
    </nav>
  </header>
  <div class="hero-copy">
    <h1 class="hero-title">Peak Forge Athletics</h1>
    <p class="hero-sub">SED UT PERSPICIATIS UNDE OMNIS ISTE NATUS ERROR SIT VOLUPTATEM</p>
  </div>
  <div class="hero-dots"><span class="on"></span><span></span></div>
</section>

<section class="welcome">
  <h2 class="section-title">Welcome to Peak Forge Athletics</h2>
  <p>Train with structured online coaching built around your goals, schedule and sport. We combine smart programming with clear nutrition guidance so every session moves you forward. Get weekly check-ins, honest feedback and a plan that adapts as you grow stronger.</p>
  <a class="btn" href="#">Click here for more info</a>
</section>

<section class="services">
  <h2 class="section-title">Our <em>Services</em></h2>
  <p class="lead">Online coaching for physique, strength and hybrid athletes who want measurable results.</p>
  <div class="service-grid">
    <div class="service">
      <svg class="service-icon" viewBox="0 0 100 100"><circle cx="50" cy="50" r="44" fill="#1b1b1b" stroke="#b5121b" stroke-width="6"/><g fill="#e9e9e9"><rect x="24" y="40" width="8" height="20"/><rect x="68" y="40" width="8" height="20"/><rect x="32" y="46" width="36" height="8"/></g></svg>
      <h3>Building Muscle Losing Fat</h3>
      <p>Lose fat and add lean muscle with a plan built around your body and routine.</p>
    </div>
    <div class="service">
      <svg class="service-icon" viewBox="0 0 100 100"><circle cx="50" cy="50" r="44" fill="#1b1b1b" stroke="#b5121b" stroke-width="6"/><g fill="#e9e9e9"><rect x="20" y="36" width="6" height="28"/><rect x="74" y="36" width="6" height="28"/><rect x="26" y="47" width="48" height="6"/><rect x="14" y="42" width="6" height="16"/><rect x="80" y="42" width="6" height="16"/></g></svg>
      <h3>Powerlifting</h3>
      <p>Structured strength blocks to raise your squat, bench and deadlift for meet day.</p>
    </div>
    <div class="service">
      <svg class="service-icon" viewBox="0 0 100 100"><circle cx="50" cy="50" r="44" fill="#1b1b1b" stroke="#b5121b" stroke-width="6"/><polyline points="22,52 36,52 42,38 52,64 58,46 64,52 78,52" fill="none" stroke="#e9e9e9" stroke-width="5" stroke-linejoin="round"/></svg>
      <h3>Hybrid Training</h3>
      <p>Build strength and endurance together, from the platform to the half marathon.</p>
    </div>
    <div class="service">
      <svg class="service-icon" viewBox="0 0 100 100"><circle cx="50" cy="50" r="44" fill="#1b1b1b" stroke="#b5121b" stroke-width="6"/><circle cx="50" cy="54" r="16" fill="none" stroke="#e9e9e9" stroke-width="5"/><rect x="47" y="26" width="6" height="14" fill="#e9e9e9"/></svg>
      <h3>Nutrition</h3>
      <p>Simple, flexible meal guidance that fuels training and supports lasting change.</p>
    </div>
  </div>
</section>

<section class="about">
  <div class="about-photo" role="img" aria-label="Powerlifter performing a heavy deadlift on a competition platform"></div>
  <div class="about-copy">
    <h2 class="section-title">About our <em>Company</em></h2>
    <p>We are a fully online coaching team helping athletes train wherever they are. Every plan is written by experienced coaches and reviewed each week to keep progress steady.</p>
    <p>Lower cost than a personal trainer, more time effective, and always tailored to your sport and goals.</p>
    <a class="btn" href="#">View more</a>
  </div>
</section>

<section class="pricing">
  <h2 class="section-title">Pricing <em>Plan</em></h2>
  <p class="lead">Pick the coaching package that fits your training and budget.</p>
  <div class="price-grid">
    <div class="plan"><span class="plan-dot"></span>
      <h3>1 Only Training Coaching</h3>
      <div class="plan-price">130 DOLLAR <small>/ PER MONTH</small></div>
      <ul><li>Custom training program</li><li>Weekly coach check-in</li><li>Video form review</li><li>Email support included</li></ul>
      <a class="btn" href="#">Get it now</a>
    </div>
    <div class="plan featured"><span class="plan-dot"></span>
      <h3>Only Nutrition Coaching</h3>
      <div class="plan-price">130 DOLLAR <small>/ PER MONTH</small></div>
      <ul><li>Personal macro targets</li><li>Weekly meal review</li><li>Flexible food guide</li><li>Email support included</li></ul>
      <a class="btn" href="#">Get it now</a>
    </div>
    <div class="plan"><span class="plan-dot"></span>
      <h3>Training + Nutrition</h3>
      <div class="plan-price">175 DOLLAR <small>/ PER MONTH</small></div>
      <ul><li>Full training program</li><li>Complete nutrition plan</li><li>Weekly video call</li><li>Priority email support</li></ul>
      <a class="btn" href="#">Get it now</a>
    </div>
  </div>
</section>

<section class="blog">
  <h2 class="section-title">Latest <em>Blog</em></h2>
  <p class="lead">Training tips, nutrition ideas and stories from our athletes.</p>
  <div class="post-grid">
    <article class="post">
      <div class="post-photo" role="img" aria-label="Athletes doing partner training in a gym" style="background:linear-gradient(135deg,#3b4656,#6a5a50)"></div>
      <h3>Neque Porro Quisquam</h3>
      <p>How to balance heavy lifting with running during a busy training week.</p>
      <time>Posted on 12 June</time>
    </article>
    <article class="post">
      <div class="post-photo" role="img" aria-label="Dumbbells on a gym floor under blue light" style="background:linear-gradient(135deg,#1d3a66,#2a2f3a)"></div>
      <h3>Neque Porro Quisquam</h3>
      <p>Five simple habits that help you drop fat while keeping your strength.</p>
      <time>Posted on 18 June</time>
    </article>
    <article class="post">
      <div class="post-photo" role="img" aria-label="Athlete curling a dumbbell in a dark gym" style="background:linear-gradient(135deg,#5a4a40,#1e1b1a)"></div>
      <h3>Neque Porro Quisquam</h3>
      <p>Preparing for your first meet: peaking, attempts and what to eat.</p>
      <time>Posted on 24 June</time>
    </article>
  </div>
</section>

<footer class="site-footer">
  <div class="social"><span></span><span></span><span></span><span></span><span></span><span></span></div>
  <nav class="foot-nav"><a href="#">HOME</a><a href="#">ABOUT US</a><a href="#">SERVICES</a><a href="#">PRICING</a><a href="#">NEWS</a><a href="#">CONTACT US</a></nav>
  <p class="copyright">© Copyright 2016 Peak Forge Athletics All Rights Reserved</p>
</footer>

</div>
</body>
</html>
```